Dune Air & Plus business card

I need an awesome, double-sided business card designed with our new logo. I would like the one side black with the colored logo, and the back side is all yours. I'd like to see horizontal and vertical layouts. Get creative! Thank you.

Target Market(s)

HVAC, Heating and Cooling in Phoenix, AZ

Industry/Entity Type

HVAC

Contact Information for Business Card

We need our new logo on the card. Tom Harker, (623) 555-0142, tom@trydunesair.com, www.trydunesair.com, ROC 514273

```html
<!DOCTYPE html>
<html lang="en">
<head>
<meta charset="utf-8">
<title>Dune Air &amp; Plus business card</title>
<link rel="stylesheet" href="https://fonts.googleapis.com/css2?family=Poppins:wght@400;700;800&family=Russo+One&display=swap">
<style>
  :root {
    --stage: #e9e9eb;
    --card-black: #1c1c1d;
    --emboss: #2e2e30;
    --white: #ffffff;
    --blue: #1f5fb4;
    --blue-deep: #17478e;
    --orange: #f07a1c;
    --orange-deep: #e2541a;
    --ink: #222222;
  }
  * { box-sizing: border-box; margin: 0; padding: 0; }
  html, body { width: 1200px; height: 1095px; overflow: hidden; }
  body {
    background: var(--stage);
    font-family: "Poppins", sans-serif;
    display: flex;
    flex-direction: column;
    align-items: center;
    justify-content: center;
    gap: 70px;
  }
  .card {
    position: relative;
    width: 700px;
    height: 400px;
    border-radius: 26px;
    overflow: hidden;
    box-shadow: 0 10px 30px rgba(0,0,0,0.18);
  }
  .card--back {
    background: var(--card-black);
    display: flex;
    align-items: center;
    justify-content: center;
  }
  .brand-name {
    font-family: "Poppins", sans-serif;
    font-weight: 800;
    letter-spacing: 0.5px;
    line-height: 1;
  }
  .card--back .brand-name {
    color: var(--emboss);
    font-size: 54px;
  }
  .card--front { background: var(--white); }
  .front-brand {
    position: absolute;
    left: 44px;
    top: 0;
    height: 100%;
    width: 300px;
    display: flex;
    align-items: center;
    gap: 14px;
  }
  .front-brand .brand-dot {
    width: 30px; height: 30px; border-radius: 50%;
    background: var(--blue);
    flex: none;
  }
  .front-brand .brand-name {
    color: var(--blue);
    font-size: 36px;
  }
  .divider {
    position: absolute;
    left: 372px;
    top: 88px;
    width: 3px;
    height: 190px;
    background: linear-gradient(var(--orange) 0 22%, transparent 22% 28%, var(--blue) 28% 72%, transparent 72% 78%, var(--orange) 78% 100%);
  }
  .contact {
    position: absolute;
    left: 402px;
    top: 80px;
  }
  .contact-name {
    font-family: "Russo One", sans-serif;
    color: var(--blue);
    font-size: 38px;
    letter-spacing: 1px;
    line-height: 1;
  }
  .contact-role {
    font-size: 16px;
    color: var(--ink);
    margin: 6px 0 14px;
  }
  .contact-list { list-style: none; }
  .contact-list li {
    display: flex;
    align-items: center;
    gap: 8px;
    font-size: 17px;
    color: var(--ink);
    letter-spacing: 0.8px;
    line-height: 1.7;
  }
  .contact-list svg { width: 16px; height: 16px; flex: none; }
  .swoosh {
    position: absolute;
    left: 0; top: 0;
    width: 700px; height: 400px;
  }
  .licence {
    position: absolute;
    right: 36px;
    bottom: 42px;
    font-family: "Russo One", sans-serif;
    color: var(--white);
    font-size: 20px;
    letter-spacing: 1px;
    transform: rotate(-14deg);
  }
</style>
</head>
<body>

  <section class="card card--back" aria-label="Card back">
    <span class="brand-name">Dune Air &amp; Plus</span>
  </section>

  <section class="card card--front" aria-label="Card front">
    <svg class="swoosh" viewBox="0 0 700 400" aria-hidden="true">
      <defs>
        <linearGradient id="band" x1="0" y1="0" x2="1" y2="0">
          <stop offset="0" stop-color="var(--orange)"/>
          <stop offset="1" stop-color="var(--orange-deep)"/>
        </linearGradient>
      </defs>
      <path d="M380,400 C500,330 600,270 700,238 L700,250 C610,280 520,340 430,400 Z" fill="var(--blue)"/>
      <path d="M440,400 C530,342 615,286 700,258 L700,400 Z" fill="url(#band)"/>
    </svg>

    <div class="front-brand">
      <span class="brand-dot"></span>
      <span class="brand-name">Dune Air &amp; Plus</span>
    </div>

    <div class="divider"></div>

    <div class="contact">
      <h1 class="contact-name">TOM HARKER</h1>
      <p class="contact-role">Director</p>
      <ul class="contact-list">
        <li>
          <svg viewBox="0 0 16 16"><path d="M4 1.5l2.2 3-1.3 1.6c.8 1.8 2.2 3.3 4 4.1l1.6-1.3 3 2.2-1.2 2.6C7 13.4 2.6 9 2 3z" fill="var(--orange)"/></svg>
          (623) 555-0142
        </li>
        <li>
          <svg viewBox="0 0 16 16"><rect x="1" y="3" width="14" height="10" fill="var(--orange)"/><path d="M1 3l7 6 7-6" fill="none" stroke="#fff" stroke-width="1.4"/></svg>
          tom@trydunesair.com
        </li>
        <li>
          <svg viewBox="0 0 16 16"><circle cx="8" cy="8" r="6.5" fill="none" stroke="var(--orange)" stroke-width="1.6"/><path d="M1.5 8h13M8 1.5c-3 3.5-3 9.5 0 13M8 1.5c3 3.5 3 9.5 0 13" fill="none" stroke="var(--orange)" stroke-width="1.2"/></svg>
          www.trydunesair.com
        </li>
      </ul>
    </div>

    <span class="licence">ROC 514273</span>
  </section>

</body>
</html>
```